Redesign of the current website

We would like a new format and redesign of the www.govanto.com website. We are a medical tech company and want our site to reflect current technology trends. VANTO provides innovative solutions to streamline business operations of Imaging Providers and Physicians while delivering life-changing solutions to patients. Free to patients and physicians.

Target Market(s)

Imaging Providers (with a secondary appeal for physicians and patients)

Industry/Entity Type

MedTech

Coding

Coded - Design and coding required

Number of Pages Required

1 page

Font styles to use
Sans Serif

Requirements
Must have
• New clear slogan to represent who and what we do.
Nice to have
• VANTO provides innovative solutions to streamline business operations of Imaging Providers and Physicians while delivering life-changing solutions to patients.
Should not have
• Social Radiology or Join the revolution

```html
<!DOCTYPE html>
<html lang="en">
<head>
<meta charset="utf-8">
<title>VANTO – Medical Imaging Platform</title>
<link href="https://fonts.googleapis.com/css2?family=Poppins:wght@400;500;600;700&display=swap" rel="stylesheet">
<style>
:root{
  --blue:#1e96dc;
  --green:#6cbd3c;
  --green-light:#d9f2c9;
  --ink:#222226;
  --text:#3b3b3b;
  --muted:#555;
  --soft:#f4f4f6;
  --footer:#232325;
  --white:#fff;
}
*{margin:0;padding:0;box-sizing:border-box}
html,body{width:1200px;height:5208px;overflow:hidden}
body{position:relative;font-family:'Poppins',sans-serif;color:var(--text);background:var(--white)}
.abs{position:absolute}
.topbar{left:0;top:0;width:1200px;height:50px;background:var(--blue);color:#fff;font-size:13px;font-weight:600;letter-spacing:.3px}
.topbar .contact{left:72px;top:16px;display:flex;gap:34px}
.topbar .contact span{display:flex;align-items:center;gap:8px}
.topbar .access{right:72px;top:17px;font-size:12px}
.logo{font-weight:700;color:var(--green);display:flex;align-items:center;gap:10px;white-space:nowrap}
.logo i{display:block;border-radius:50%;background:var(--blue)}
.logo small{display:block;font-size:9px;color:var(--blue);font-weight:600;letter-spacing:1.5px}
.nav{right:72px;top:80px;display:flex;gap:34px;font-size:13px;font-weight:600;color:var(--ink)}
.nav .active{color:var(--blue)}
.hero-title{left:75px;top:236px}
.hero-title div{background:#111;color:#fff;display:inline-block;padding:2px 10px;margin-bottom:6px;font-weight:500;white-space:nowrap}
.btn{display:flex;align-items:center;justify-content:center;background:var(--green);color:#fff;font-weight:600;font-size:17px;border-radius:30px;height:58px;box-shadow:0 4px 10px rgba(0,0,0,.12)}
.h-blue{color:var(--blue);font-weight:700;white-space:nowrap}
.para{font-size:16px;line-height:35px;color:var(--text)}
.band-title{width:1200px;text-align:center;color:#fff;font-weight:700;font-size:41px;line-height:48px}
.feature{background:#fff;border-radius:8px;box-shadow:0 4px 18px rgba(0,0,0,.15);text-align:center;padding:30px 26px}
.feature h3{color:var(--blue);font-size:22px;line-height:29px;font-weight:700;margin:26px 0 14px}
.feature p{font-size:14.5px;line-height:28.5px;color:var(--muted)}
.pcard{width:512px;height:145px;background:#fff;border-radius:8px;display:flex;align-items:center;padding:0 22px;gap:30px;font-size:14.5px;line-height:27px;color:#333}
.pcard .ic{flex:none;width:100px;height:100px;border-radius:14px;background:var(--green-light);display:flex;align-items:center;justify-content:center}
.review{left:162px;top:4258px;width:874px;height:290px;background:#fff;box-shadow:0 4px 16px rgba(0,0,0,.15);text-align:center}
.review:before,.review:after{content:"";position:absolute;left:0;right:0;height:7px;background:linear-gradient(90deg,var(--green),var(--blue))}
.review:before{top:0}.review:after{bottom:0}
.footer h4{color:#fff;font-size:21px;font-weight:600;margin-bottom:12px;white-space:nowrap}
.footer p,.footer li{font-size:13px;line-height:27px;color:#ddd;list-style:none}
</style>
</head>
<body>

<div class="abs topbar">
  <div class="abs contact">
    <span><svg width="14" height="14" viewBox="0 0 24 24"><path fill="#fff" d="M6.6 10.8a15 15 0 0 0 6.6 6.6l2.2-2.2a1 1 0 0 1 1-.25 11.4 11.4 0 0 0 3.6.57 1 1 0 0 1 1 1V20a1 1 0 0 1-1 1A17 17 0 0 1 3 4a1 1 0 0 1 1-1h3.5a1 1 0 0 1 1 1c0 1.25.2 2.45.57 3.57a1 1 0 0 1-.25 1z"/></svg>1-800-555-0148</span>
    <span><svg width="14" height="14" viewBox="0 0 24 24"><path fill="#fff" d="M2 5h20v14H2zm2 2v.5l8 5 8-5V7z"/></svg>info@govanto.com</span>
  </div>
  <div class="abs access">LOGIN &nbsp;/&nbsp; REGISTER &nbsp;/&nbsp; PHYSICIAN GUEST ACCESS</div>
</div>

<!-- hero -->
<svg class="abs" style="left:0;top:50px" width="1200" height="700" viewBox="0 0 1200 700" aria-hidden="true">
  <defs>
    <linearGradient id="heroPhoto" x1="0" y1="0" x2="1" y2="1">
      <stop offset="0" stop-color="#eef1f5"/><stop offset=".6" stop-color="#cfd8e2"/><stop offset="1" stop-color="#9aa7b5"/>
    </linearGradient>
    <linearGradient id="softBg" x1="0" y1="0" x2="0" y2="1">
      <stop offset="0" stop-color="#fff"/><stop offset="1" stop-color="#f5f3fb"/>
    </linearGradient>
  </defs>
  <rect width="1200" height="700" fill="url(#softBg)"/>
  <path d="M318 0 C370 160 470 300 610 360 C760 420 830 560 990 650 C1090 700 1170 680 1200 640 L1200 0 Z" fill="#6cbd3c"/>
  <path d="M318 0 C370 150 470 285 605 345 C755 405 825 545 985 630 C1080 675 1165 660 1200 625 L1200 0 Z" fill="url(#heroPhoto)" role="img" aria-label="Photo of a doctor using a tablet with floating medical icons"/>
</svg>
<div class="abs logo" style="left:72px;top:70px;font-size:40px">VANTO<i style="width:14px;height:14px"></i></div>
<div class="abs logo" style="left:116px;top:140px"><small>WWW.GOVANTO.COM</small></div>
<nav class="abs nav"><span class="active">HOME</span><span>SOLUTION</span><span>STORAGE</span><span>NEWS ROOM</span><span>COMPANY</span></nav>
<div class="abs hero-title">
  <div style="font-size:62px;line-height:66px;font-weight:700">VANTO</div><br>
  <div style="font-size:38px;line-height:50px">Imaging, Connected</div><br>
  <div style="font-size:38px;line-height:50px">Free For Patients!</div>
</div>
<div class="abs btn" style="left:75px;top:456px;width:205px">Read More</div>

<!-- thinking ahead -->
<svg class="abs" style="left:0;top:705px" width="500" height="640" aria-hidden="true">
  <defs><linearGradient id="skel" x1="0" y1="0" x2="1" y2="1"><stop offset="0" stop-color="#0b2d63"/><stop offset=".5" stop-color="#1f6fc4"/><stop offset="1" stop-color="#0a2a55"/></linearGradient></defs>
  <circle cx="175" cy="315" r="320" fill="#6cbd3c"/>
  <circle cx="170" cy="315" r="318" fill="url(#skel)" role="img" aria-label="Photo of a glowing digital skeleton model with medical equipment"/>
</svg>
<h2 class="abs h-blue" style="left:560px;top:838px;font-size:43px">Thinking Ahead</h2>
<p class="abs para" style="left:560px;top:908px;width:568px">There are so many competing pressures on healthcare providers today; meaningful use, data security, managing costs and of course increasing revenue. Solving all of these issues can sometimes seem like a mine field… what systems should I buy, how do I ensure data security while exposing it in patient or physician portals, how can I maintain or reduce my costs while meeting all of these requirements.</p>
<div class="abs btn" style="left:560px;top:1188px;width:207px">Read More</div>

<!-- cost band -->
<svg class="abs" style="left:0;top:1310px" width="1200" height="645" aria-hidden="true">
  <defs><linearGradient id="band" x1="0" y1="0" x2="1" y2="0"><stop offset="0" stop-color="#6cbd3c"/><stop offset=".5" stop-color="#3aab8c"/><stop offset="1" stop-color="#1e96dc"/></linearGradient></defs>
  <path d="M0 210 C180 90 360 100 560 150 C780 210 960 180 1200 20 L1200 645 L0 645 Z" fill="url(#band)"/>
</svg>
<h2 class="abs band-title" style="left:0;top:1546px">Lower your costs while streamlining<br>the diagnosis</h2>
<div class="abs feature" style="left:254px;top:1685px;width:332px;height:445px">
  <svg width="150" height="150" viewBox="0 0 150 150" aria-hidden="true"><path d="M40 18 C80 4 128 20 140 60 C150 100 118 140 76 140 C34 140 6 110 10 70 C12 42 22 25 40 18Z" fill="#6cbd3c" opacity=".85"/><path d="M60 12 C100 10 140 40 132 86 C126 126 90 146 56 132 C22 118 14 80 24 50 C30 30 42 14 60 12Z" fill="#1e96dc" opacity=".35"/><rect x="34" y="42" width="82" height="58" rx="4" fill="none" stroke="#222" stroke-width="3"/><path d="M66 100 L62 116 H88 L84 100 M54 116 H96" stroke="#222" stroke-width="3" fill="none"/><path d="M44 88 L62 64 L78 80 L104 52" stroke="#222" stroke-width="3" fill="none"/></svg>
  <h3>Streamlined Diagnosis<br>&amp; Decision Making</h3>
  <p>Diagnosis &amp; decision-making are streamlined. Hard copy production costs can now be eliminated with VANTO’s cloud-based service that is also PACS compatible.</p>
</div>
<div class="abs feature" style="left:614px;top:1685px;width:332px;height:445px">
  <svg width="150" height="150" viewBox="0 0 150 150" aria-hidden="true"><path d="M40 18 C80 4 128 20 140 60 C150 100 118 140 76 140 C34 140 6 110 10 70 C12 42 22 25 40 18Z" fill="#6cbd3c" opacity=".85"/><path d="M60 12 C100 10 140 40 132 86 C126 126 90 146 56 132 C22 118 14 80 24 50 C30 30 42 14 60 12Z" fill="#1e96dc" opacity=".35"/><path d="M38 114 H114" stroke="#222" stroke-width="3"/><rect x="44" y="78" width="12" height="34" fill="none" stroke="#222" stroke-width="3"/><rect x="66" y="64" width="12" height="48" fill="none" stroke="#222" stroke-width="3"/><rect x="88" y="70" width="12" height="42" fill="none" stroke="#222" stroke-width="3"/><path d="M46 60 L72 42 L94 52 L110 36" stroke="#222" stroke-width="3" fill="none"/><circle cx="72" cy="42" r="4" fill="#222"/><circle cx="94" cy="52" r="4" fill="#222"/></svg>
  <h3>Real-Time Access to<br>Historical Records</h3>
  <p>All participants now have real-time access to historical records &amp; business intelligence tools that eliminate overhead costs &amp; improve the quality of Patient Care.</p>
</div>

<!-- empower -->
<svg class="abs" style="left:700px;top:2140px" width="500" height="625" aria-hidden="true">
  <defs><linearGradient id="tab" x1="0" y1="0" x2="1" y2="1"><stop offset="0" stop-color="#0d3354"/><stop offset=".5" stop-color="#2a7ab3"/><stop offset="1" stop-color="#a9c8de"/></linearGradient></defs>
  <circle cx="320" cy="312" r="312" fill="#6cbd3c"/>
  <circle cx="326" cy="308" r="310" fill="url(#tab)" role="img" aria-label="Photo of a doctor holding a tablet with holographic body scan"/>
</svg>
<div class="abs" style="left:75px;top:2268px;font-size:35px;line-height:44px;color:var(--green);font-weight:500">Thinking Ahead</div>
<h2 class="abs h-blue" style="left:75px;top:2312px;font-size:41px;line-height:44px">Empower Patients<br>&amp; Healthcare Providers</h2>
<p class="abs para" style="left:75px;top:2422px;width:565px">VANTO allows the ownership of the images to be in the Patient’s hands and enables interoperability between Diagnostic Imaging Centers, Patients and Physicians.</p>
<div class="abs btn" style="left:75px;top:2574px;width:205px">Read More</div>

<!-- problem / solution -->
<svg class="abs" style="left:0;top:2780px" width="1200" height="940" aria-hidden="true">
  <path d="M0 40 C300 0 700 120 1200 30 L1200 940 L0 940 Z" fill="#f4f4f6"/>
</svg>
<h2 class="abs h-blue" style="left:74px;top:2916px;font-size:41px">Problem</h2>
<h2 class="abs h-blue" style="left:612px;top:2916px;font-size:41px">Solution</h2>

<div class="abs pcard" style="left:74px;top:3002px"><div class="ic"><svg width="44" height="44" viewBox="0 0 24 24"><circle cx="12" cy="12" r="9" fill="none" stroke="#6cbd3c" stroke-width="2.2"/><path d="M12 7v5l3 3" stroke="#6cbd3c" stroke-width="2.2" fill="none"/></svg></div><span>No real-time solutions today for sharing radiology images and reports between physicians, imaging providers and patients</span></div>
<div class="abs pcard" style="left:74px;top:3173px"><div class="ic"><svg width="50" height="44" viewBox="0 0 26 22"><rect x="5" y="1" width="20" height="15" rx="2" fill="#6cbd3c"/><rect x="1" y="5" width="20" height="15" rx="2" fill="#fff" stroke="#6cbd3c" stroke-width="2"/><path d="M4 17 L9 11 L13 15 L16 12 L19 17Z" fill="#6cbd3c"/></svg></div><span>Too much duplication of imaging</span></div>
<div class="abs pcard" style="left:74px;top:3345px"><div class="ic"><svg width="42" height="44" viewBox="0 0 24 24"><path d="M12 2a2 2 0 0 1 2 2 7 7 0 0 1 5 7v5l2 2v1H3v-1l2-2v-5a7 7 0 0 1 5-7 2 2 0 0 1 2-2zm-2 19h4a2 2 0 0 1-4 0z" fill="#6cbd3c"/></svg></div><span>No notification to the patient following physician review of image and report</span></div>
<div class="abs pcard" style="left:74px;top:3516px"><div class="ic"><svg width="50" height="44" viewBox="0 0 26 22"><rect x="4" y="2" width="18" height="13" rx="1.5" fill="none" stroke="#6cbd3c" stroke-width="2.4"/><path d="M1 18h24v2H1z" fill="#6cbd3c"/></svg></div><span>Too many manual processes today in order for providers to access patient images and reports</span></div>

<div class="abs pcard" style="left:614px;top:3002px"><div class="ic"><svg width="54" height="40" viewBox="0 0 26 18"><path d="M7 17a6 6 0 0 1-.6-11.9A7 7 0 0 1 19.5 5 6 6 0 0 1 20 17z" fill="#6cbd3c"/></svg></div><span>Secure Web-based Cloud platform that provides sharing images and reports</span></div>
<div class="abs pcard" style="left:614px;top:3173px"><div class="ic"><svg width="30" height="50" viewBox="0 0 14 24"><path d="M11 6.5C10.5 5 9 4 7 4 4.8 4 3 5.3 3 7.2c0 4.6 8.5 2.8 8.5 7.8 0 2.1-2 3.6-4.5 3.6-2.4 0-4.1-1.1-4.6-3M7 1v22" stroke="#6cbd3c" stroke-width="2.4" fill="none" stroke-linecap="round"/></svg></div><span>Eliminated localized storage costs</span></div>
<div class="abs pcard" style="left:614px;top:3345px"><div class="ic"><svg width="44" height="44" viewBox="0 0 24 24"><circle cx="12" cy="7.5" r="5" fill="#6cbd3c"/><path d="M2 22c0-5.5 4.5-8 10-8s10 2.5 10 8z" fill="#6cbd3c"/></svg></div><span>Patient owns the image and report and optionally assigns rights to providers</span></div>
<div class="abs pcard" style="left:614px;top:3516px"><div class="ic"><svg width="38" height="44" viewBox="0 0 20 24"><path d="M5 10V7a5 5 0 0 1 10 0v3" stroke="#6cbd3c" stroke-width="2.6" fill="none"/><rect x="2" y="10" width="16" height="13" rx="2" fill="#6cbd3c"/></svg></div><span>Provides secure audit trail</span></div>

<!-- cta band -->
<svg class="abs" style="left:0;top:3660px" width="1200" height="460" aria-hidden="true">
  <path d="M0 200 C180 150 320 220 560 200 C820 180 1020 140 1200 20 L1200 460 L0 460 Z" fill="url(#band)"/>
</svg>
<h2 class="abs band-title" style="left:0;top:3902px">Find Out How Vanto Can Help You</h2>
<div class="abs" style="left:498px;top:3990px;width:204px;height:54px;border:2px solid #fff;border-radius:30px;color:#fff;font-weight:600;font-size:17px;display:flex;align-items:center;justify-content:center">Contact Us</div>

<!-- reviews -->
<h2 class="abs h-blue" style="left:0;top:4170px;width:1200px;text-align:center;font-size:41px">Patient Reviews</h2>
<svg class="abs" style="left:0;top:4430px" width="1200" height="778" aria-hidden="true">
  <path d="M0 120 C200 60 400 40 620 130 C820 210 1000 180 1200 100 L1200 778 L0 778 Z" fill="#232325"/>
</svg>
<div class="abs review">
  <svg class="abs" style="left:18px;top:20px" width="80" height="60" aria-hidden="true"><text x="0" y="80" font-size="130" fill="#e4e4e4" font-family="Georgia,serif">“</text></svg>
  <p style="position:absolute;left:48px;right:48px;top:62px;font-size:21px;line-height:41px;color:#333">VANTO offers superior real-time online delivery service that helped my Doctor work effectively. VANTO is easily available to providers no matter where I’m located.</p>
  <div style="position:absolute;left:0;right:0;top:196px;color:var(--green);font-weight:600;font-size:19px">Name Heading</div>
  <div style="position:absolute;left:0;right:0;top:226px;color:var(--blue);font-size:14px">Location Name</div>
  <svg class="abs" style="right:30px;top:170px" width="90" height="80" aria-hidden="true"><text x="0" y="105" font-size="130" fill="#e4e4e4" font-family="Georgia,serif">”</text></svg>
</div>
<svg class="abs" style="left:104px;top:4374px" width="28" height="48" aria-hidden="true"><path d="M24 4 L6 24 L24 44" stroke="#999" stroke-width="4" fill="none"/></svg>
<svg class="abs" style="left:1062px;top:4374px" width="28" height="48" aria-hidden="true"><path d="M4 4 L22 24 L4 44" stroke="#999" stroke-width="4" fill="none"/></svg>

<!-- footer -->
<div class="abs" style="left:180px;top:4766px;color:#fff;font-size:27px;font-weight:600">Email Subscribe</div>
<div class="abs" style="left:438px;top:4760px;width:424px;height:52px;background:#fff;border-radius:28px;padding:15px 26px;font-size:14px;color:#666">Enter Email Address</div>
<div class="abs btn" style="left:878px;top:4760px;width:174px;height:52px;font-size:15px">SUBSCRIBE</div>
<div class="abs" style="left:70px;top:4880px;width:1060px;height:1px;background:#444"></div>

<div class="abs footer" style="left:0;top:0">
  <div class="abs logo" style="left:72px;top:4990px;font-size:50px">VANTO<i style="width:18px;height:18px"></i></div>
  <div class="abs logo" style="left:136px;top:5062px"><small>WWW.GOVANTO.COM</small></div>
  <div class="abs" style="left:343px;top:4913px;width:245px"><h4>About Us</h4><p>VANTO places the ownership of the images in the Patient’s hands and enables interoperability between multiple healthcare providers, payers &amp; diagnostic imaging entities.</p></div>
  <div class="abs" style="left:680px;top:4913px;width:160px"><h4>Site Map</h4><ul><li>Home</li><li>Solution</li><li>Storage</li><li>News Room</li><li>Company</li><li>Register</li></ul></div>
  <div class="abs" style="left:884px;top:4913px;width:240px"><h4>Follow Us</h4>
    <div style="display:flex;gap:18px;margin:6px 0 18px" aria-label="Social links">
      <span style="width:22px;height:22px;border-radius:50%;background:#fff"></span><span style="width:22px;height:22px;border-radius:50%;background:#fff"></span><span style="width:22px;height:22px;border-radius:50%;background:#fff"></span><span style="width:22px;height:22px;border-radius:50%;background:#fff"></span><span style="width:22px;height:22px;border-radius:50%;background:#fff"></span>
    </div>
    <p style="line-height:22px">Copyright © 2022, Company Name<br>All Right reserved</p>
  </div>
</div>
</body>
</html>
```